Menu Design Project

Bel Roux hair and beauty service menu
we need a menu to display a handful of our services to give our customers an idea of our pricing

Cutting
Ladies cuts from $35
Men's cuts from $25
All cuts are included with a wash and dry off

Velora colours
All over colours start from $55
price will vary depending upon length and thickness of hair

Foiling
starts from $50
Price will vary depending upon length of hair

Toners
from $30

Blowdries
from $35

Upstyling
wedding styling from $45
Please enquire for special occasion styling also

Beauty Services

Waxing
Eyebrow wax and shape $17.50
Lip $10
Chin/sides $20
Legs from $25
Bikini $20
XX $30
XXX $45
Back from $25
Chest from $25

Eyes
Eyebrow tinting $15
Eyelash tinting $20
Eyelash extensions from $90

Derminia facials
Express facial $45
Deluxe facial $95

Acrylic nails
full set $60
Gel polish $35
Manicures from $35
Pedicures from $45

can provide logo and other images to help

Industry/Entity Type

Hair

Requirements
Must have
• must be called a service menu
must be eye catching and memorable but not excessive
Nice to have
• postcard style size hair menu on one side
beauty menu on the other side
elegant classy design
Should not have
• must not be called a price list
stay away from traditional price list style in terms of folding out leaflet

```html
<!DOCTYPE html>
<html lang="en">
<head>
<meta charset="utf-8">
<title>Bel Roux – Service Menu</title>
<link href="https://fonts.googleapis.com/css2?family=Quicksand:wght@400;500&display=swap" rel="stylesheet">
<style>
  :root {
    --ink-dark: #07060d;
    --title-yellow: #f6ee4a;
    --text-light: #ffffff;
    --cutting-orange: #e0612b;
    --colour-blue: #2443b7;
    --toner-sky: #3fb7e4;
    --foiling-magenta: #b12ac6;
    --blowdry-lime: #a9dc3b;
    --upstyle-green: #1f8a57;
    --glow: rgba(255, 255, 255, 0.85);
  }
  html, body {
    margin: 0;
    padding: 0;
    overflow: hidden;
    background: var(--ink-dark);
  }
  .menu {
    position: relative;
    width: 848px;
    height: 1200px;
    overflow: hidden;
    font-family: "Quicksand", "Century Gothic", sans-serif;
    color: var(--text-light);
  }
  .menu__backdrop {
    position: absolute;
    inset: 0;
    background:
      radial-gradient(circle at 8% 12%, rgba(230, 110, 40, 0.55), transparent 32%),
      radial-gradient(circle at 60% 4%, rgba(200, 40, 160, 0.45), transparent 30%),
      radial-gradient(circle at 95% 15%, rgba(120, 60, 220, 0.55), transparent 30%),
      radial-gradient(circle at 12% 50%, rgba(150, 40, 190, 0.45), transparent 30%),
      radial-gradient(circle at 90% 45%, rgba(40, 120, 220, 0.5), transparent 30%),
      radial-gradient(circle at 95% 85%, rgba(120, 210, 60, 0.5), transparent 32%),
      radial-gradient(circle at 20% 90%, rgba(30, 140, 170, 0.4), transparent 30%),
      var(--ink-dark);
  }
  .menu__title {
    position: absolute;
    top: 62px;
    left: 0;
    width: 100%;
    margin: 0;
    text-align: center;
    font-weight: 400;
    font-size: 47px;
    letter-spacing: 1px;
    color: var(--title-yellow);
    text-shadow: 0 0 10px rgba(255, 240, 80, 0.5);
  }
  .service {
    position: absolute;
    border-radius: 50%;
    box-sizing: border-box;
    border: 3px solid var(--glow);
    box-shadow: 0 0 18px 4px rgba(255, 255, 255, 0.45), inset 0 0 22px rgba(255, 255, 255, 0.25);
    display: flex;
    flex-direction: column;
    align-items: center;
    justify-content: center;
    text-align: center;
    padding: 0;
    white-space: nowrap;
    text-shadow: 1px 2px 3px rgba(0, 0, 0, 0.55);
  }
  .service__name {
    margin: 0 0 12px;
    font-weight: 500;
    font-size: 36px;
    line-height: 1.1;
  }
  .service__price {
    margin: 0;
    font-size: 25px;
    line-height: 1.4;
  }
  .service__note {
    margin: 8px 0 0;
    font-size: 18px;
    line-height: 1.45;
  }
  .service--cutting   { left: 46px;  top: 154px; width: 320px; height: 320px; background: var(--cutting-orange); }
  .service--colours   { left: 485px; top: 149px; width: 322px; height: 322px; background: var(--colour-blue); }
  .service--toners    { left: 316px; top: 404px; width: 228px; height: 228px; background: var(--toner-sky); }
  .service--foiling   { left: 46px;  top: 584px; width: 320px; height: 320px; background: var(--foiling-magenta); }
  .service--blowdries { left: 498px; top: 594px; width: 300px; height: 300px; background: var(--blowdry-lime); }
  .service--upstyling { left: 280px; top: 862px; width: 300px; height: 300px; background: var(--upstyle-green); }

  .service--cutting { padding-bottom: 14px; }
  .service--colours .service__name { font-size: 33px; margin-bottom: 10px; }
  .service--colours .service__price { font-size: 22px; }
  .service--colours .service__note { font-size: 17px; line-height: 1.4; }
  .service--toners .service__name { margin-bottom: 6px; }
  .service--foiling .service__note { font-size: 17px; }
  .service--blowdries .service__price { font-size: 24px; }
  .service--blowdries .service__note { font-size: 16px; }
  .service--upstyling .service__price { font-size: 22px; }
  .service--upstyling .service__note { font-size: 15px; margin-top: 2px; }
</style>
</head>
<body>
<main class="menu">
  <div class="menu__backdrop" role="img" aria-label="Dark background with soft multicoloured bokeh light circles"></div>
  <h1 class="menu__title">service menu</h1>

  <section class="service service--cutting">
    <h2 class="service__name">Cutting</h2>
    <p class="service__price">Ladies cuts from $35<br>Men's cuts from $25</p>
    <p class="service__note">All cuts are included with<br>a wash and dry off</p>
  </section>

  <section class="service service--colours">
    <h2 class="service__name">Velora colours</h2>
    <p class="service__price">All over colours start from<br>$55</p>
    <p class="service__note">Price will vary depending<br>upon length and thickness<br>of hair</p>
  </section>

  <section class="service service--toners">
    <h2 class="service__name">Toners</h2>
    <p class="service__price">From $30</p>
  </section>

  <section class="service service--foiling">
    <h2 class="service__name">Foiling</h2>
    <p class="service__price">Starts from $50</p>
    <p class="service__note">Price will vary depending upon<br>length of hair</p>
  </section>

  <section class="service service--blowdries">
    <h2 class="service__name">Blowdries</h2>
    <p class="service__price">From $35</p>
    <p class="service__note">Price will vary depending upon<br>length and thickness of hair</p>
  </section>

  <section class="service service--upstyling">
    <h2 class="service__name">Upstyling</h2>
    <p class="service__price">Wedding styling from $45</p>
    <p class="service__note">Please enquire for special occasion<br>styling also</p>
  </section>
</main>
</body>
</html>
```